Professional business cards for real estate development company

I need business cards for my new real estate development company. The company, "KORVA" is a real estate development, investment, and advisory firm with a focus on multifamily, office, and mixed-use projects across primary and secondary markets in the Southeast United States.

Style preference is modern

Industry/Entity Type

Real Estate Development

Contact Information for Business Card

The business cards need to include:
Name
Title
Mailing Address
Phone Number
Web Address

Logo is attached. I would like white to be the primary color with incorporation of the company colors: #232D3A and #B5A451

Font styles to use
Other font styles liked:
• Montserrat, Avenir

Requirements
Must have
• Company Logo. No need to include the company name since the name is in the logo.
Should not have
• No line type designs

```html
<!DOCTYPE html>
<html lang="en">
<head>
<meta charset="utf-8">
<title>KORVA Business Cards</title>
<link rel="stylesheet" href="https://fonts.googleapis.com/css2?family=Nunito+Sans:wght@400;600;700&display=swap">
<style>
  :root {
    --navy: #232d3a;
    --gold: #b5a451;
    --card: #ffffff;
    --card-edge: #d6d9de;
    --backdrop: #e4e5e7;
  }
  * { margin: 0; padding: 0; box-sizing: border-box; }
  html, body {
    width: 1200px;
    height: 923px;
    overflow: hidden;
    background: var(--backdrop);
    font-family: "Nunito Sans", "Avenir", sans-serif;
  }
  .canvas { position: relative; width: 1200px; height: 923px; }
  .card {
    position: absolute;
    left: 290px;
    width: 621px;
    height: 355px;
    background: var(--card);
    border: 1px solid var(--card-edge);
  }
  .card--front { top: 83px; }
  .card--back { top: 485px; }

  .front-wordmark {
    position: absolute;
    inset: 0;
    display: flex;
    align-items: center;
    justify-content: center;
    font-weight: 400;
    font-size: 64px;
    letter-spacing: 4px;
    color: var(--navy);
  }

  .back-wordmark {
    position: absolute;
    left: 52px;
    width: 210px;
    top: 0;
    height: 355px;
    display: flex;
    align-items: center;
    justify-content: center;
    font-weight: 400;
    font-size: 46px;
    letter-spacing: 3px;
    color: var(--navy);
  }

  .divider {
    position: absolute;
    left: 311px;
    top: 67px;
    width: 2px;
    height: 222px;
    background: var(--gold);
  }

  .contact {
    position: absolute;
    left: 345px;
    top: 66px;
    color: var(--navy);
  }
  .contact__name {
    font-weight: 700;
    font-size: 19px;
    letter-spacing: 0.3px;
    line-height: 1.2;
    color: var(--gold);
  }
  .contact__title {
    font-size: 14px;
    line-height: 1.3;
    margin-top: 1px;
  }
  .contact__address {
    font-size: 16.5px;
    line-height: 23px;
    letter-spacing: 0.3px;
    margin-top: 16px;
  }
  .contact__list {
    list-style: none;
    margin-top: 14px;
  }
  .contact__item {
    display: flex;
    align-items: center;
    height: 27.5px;
    font-size: 16.5px;
    letter-spacing: 0.3px;
  }
  .contact__icon {
    width: 18px;
    height: 18px;
    margin-right: 13px;
    fill: var(--gold);
    flex: none;
  }
</style>
</head>
<body>
<main class="canvas">
  <section class="card card--front" aria-label="Card front">
    <div class="front-wordmark">KORVA</div>
  </section>

  <section class="card card--back" aria-label="Card back">
    <div class="back-wordmark">KORVA</div>
    <div class="divider"></div>
    <div class="contact">
      <p class="contact__name">DANIEL HARLOW</p>
      <p class="contact__title">Founder | CEO</p>
      <p class="contact__address">218 Meridian Street, Ashford<br>KY, 40512</p>
      <ul class="contact__list">
        <li class="contact__item">
          <svg class="contact__icon" viewBox="0 0 24 24" aria-hidden="true"><path d="M6.6 10.8a15.1 15.1 0 0 0 6.6 6.6l2.2-2.2a1 1 0 0 1 1-.25 11.4 11.4 0 0 0 3.6.57 1 1 0 0 1 1 1V20a1 1 0 0 1-1 1A17 17 0 0 1 3 4a1 1 0 0 1 1-1h3.5a1 1 0 0 1 1 1c0 1.25.2 2.450.57 3.57a1 1 0 0 1-.25 1z"/></svg>
          502-555-0148
        </li>
        <li class="contact__item">
          <svg class="contact__icon" viewBox="0 0 24 24" aria-hidden="true"><path d="M8 1h8a2 2 0 0 1 2 2v18a2 2 0 0 1-2 2H8a2 2 0 0 1-2-2V3a2 2 0 0 1 2-2zm0 3v14h8V4zm4 15.2a1 1 0 1 0 0 2 1 1 0 0 0 0-2z"/></svg>
          206-555-0173
        </li>
        <li class="contact__item">
          <svg class="contact__icon" viewBox="0 0 24 24" aria-hidden="true"><path d="M2 6a1 1 0 0 1 1-1h18a1 1 0 0 1 1 1v.4l-10 6-10-6zm0 2.7 10 6 10-6V18a1 1 0 0 1-1 1H3a1 1 0 0 1-1-1z"/></svg>
          harlow@korva-mail.net
        </li>
        <li class="contact__item">
          <svg class="contact__icon" viewBox="0 0 24 24" aria-hidden="true"><path d="M12 2a10 10 0 1 0 0 20 10 10 0 0 0 0-20zm0 2c.9 0 2.1 1.7 2.7 5H9.3C9.9 5.7 11.1 4 12 4zM4.3 10h3c-.1 1.3-.1 2.7 0 4h-3a8 8 0 0 1 0-4zm5 0h5.4c.1 1.3.1 2.7 0 4H9.3c-.1-1.3-.1-2.7 0-4zm7.4 0h3a8 8 0 0 1 0 4h-3c.1-1.3.1-2.7 0-4zM9.3 15h5.4c-.6 3.3-1.8 5-2.7 5s-2.1-1.7-2.7-5z"/></svg>
          www.korvadev.net
        </li>
      </ul>
    </div>
  </section>
</main>
</body>
</html>
```